Partial Wrap Design for Painting Company

Need a wrap design that we can adapt to several vans. The immediate need is for 2016 Harlow KT300 and 2009 Brandt M-340. Vehicles are white.
We want a PARTIAL wrap (not full coverage).
We want to show;
- our phone number; (927) 555-LARK
- our website address; www.larkpainting.example
- our services; Interior - Exterior - Cabinet
Any questions? Feel free to ask.

Target Market(s)

Homeowners

Industry/Entity Type

Painting

```html
<!DOCTYPE html>
<html lang="en">
<head>
<meta charset="utf-8">
<title>Lark Painting – Partial Van Wrap Layouts</title>
<link rel="stylesheet" href="https://fonts.googleapis.com/css2?family=Open+Sans:wght@600;700;800&display=swap">
<style>
  :root {
    --backdrop: #f3f3f1;
    --guide: #c9c9c4;
    --blue: #5aaed6;
    --orange: #eea13e;
    --green: #93c83e;
    --ink: #ffffff;
  }
  * { margin: 0; padding: 0; box-sizing: border-box; }
  html, body { width: 1200px; height: 966px; overflow: hidden; }
  body {
    background: var(--backdrop);
    font-family: "Open Sans", Arial, sans-serif;
    position: relative;
  }
  .layout { position: absolute; inset: 0; }
  .zone {
    position: absolute;
    border: 2px dashed var(--guide);
  }
  .side-zone  { left: 177px; top: 112px; width: 840px; height: 300px; border-radius: 40px 120px 24px 24px; }
  .rear-zone  { left: 240px; top: 530px; width: 312px; height: 262px; border-radius: 36px 36px 12px 12px; }
  .hood-zone  { left: 690px; top: 600px; width: 310px; height: 110px; border-radius: 60px 60px 20px 20px; }
  .band {
    position: absolute;
    display: flex;
    align-items: center;
    color: var(--ink);
    font-weight: 700;
    white-space: nowrap;
  }
  .band svg.stroke { position: absolute; inset: 0; width: 100%; height: 100%; z-index: 0; }
  .band .label { position: relative; z-index: 1; display: flex; align-items: center; gap: 8px; }
  .band .icon { flex: none; }
  .services { transform: rotate(-5deg); transform-origin: left center; }
  .wordmark {
    position: absolute;
    font-weight: 800;
    color: var(--blue);
    letter-spacing: 0.02em;
    line-height: 1;
  }
  .fill-blue   { fill: var(--blue); }
  .fill-orange { fill: var(--orange); }
  .fill-green  { fill: var(--green); }
</style>
</head>
<body>

<svg width="0" height="0" style="position:absolute">
  <defs>
    <path id="brush" d="M3,5 L94,0 L100,3 L96,6 L99,10 L94,14 L98,17 L92,19 L5,20 L0,17 L6,14 L1,11 L5,8 L0,6 Z"/>
    <g id="phone-icon" fill="none" stroke="#fff" stroke-width="1.6">
      <circle cx="10" cy="10" r="8.5"/>
      <path d="M6.5,6 q0.8,-1 2,0 l1,1.6 q0.4,0.8 -0.5,1.5 q0.8,1.9 2.4,2.9 q0.8,-0.9 1.6,-0.4 l1.5,1 q0.9,1 -0.1,2 q-2,1.5 -5,-1.3 q-3.6,-3.6 -2.9,-7.3 z" fill="#fff" stroke="none"/>
    </g>
    <g id="web-icon" fill="none" stroke="#fff" stroke-width="1.4">
      <circle cx="10" cy="10" r="8.5"/>
      <ellipse cx="10" cy="10" rx="3.8" ry="8.5"/>
      <line x1="1.5" y1="10" x2="18.5" y2="10"/>
      <line x1="3" y1="5.5" x2="17" y2="5.5"/>
      <line x1="3" y1="14.5" x2="17" y2="14.5"/>
    </g>
  </defs>
</svg>

<!-- Side layout -->
<section class="layout side-layout" aria-label="Side panel layout">
  <div class="zone side-zone" aria-hidden="true"></div>

  <div class="band services" style="left:203px; top:128px; width:312px; height:62px; font-size:18px;">
    <svg class="stroke" viewBox="0 0 100 20" preserveAspectRatio="none"><use href="#brush" class="fill-blue"/></svg>
    <span class="label" style="padding-left:22px;">Interior - Exterior - Cabinet</span>
  </div>

  <div class="wordmark" style="left:232px; top:196px; font-size:110px;">Lark</div>

  <div class="band" style="left:490px; top:309px; width:334px; height:42px; font-size:17px;">
    <svg class="stroke" viewBox="0 0 100 20" preserveAspectRatio="none"><use href="#brush" class="fill-orange"/></svg>
    <span class="label" style="padding-left:36px;"><svg class="icon" width="20" height="20" viewBox="0 0 20 20"><use href="#phone-icon"/></svg>(927) 555-LARK</span>
  </div>

  <div class="band" style="left:406px; top:344px; width:400px; height:44px; font-size:17px;">
    <svg class="stroke" viewBox="0 0 100 20" preserveAspectRatio="none"><use href="#brush" class="fill-green"/></svg>
    <span class="label" style="padding-left:120px;"><svg class="icon" width="20" height="20" viewBox="0 0 20 20"><use href="#web-icon"/></svg>www.larkpainting.example</span>
  </div>
</section>

<!-- Rear layout -->
<section class="layout rear-layout" aria-label="Rear door layout">
  <div class="zone rear-zone" aria-hidden="true"></div>

  <div class="band services" style="left:250px; top:566px; width:224px; height:42px; font-size:12px;">
    <svg class="stroke" viewBox="0 0 100 20" preserveAspectRatio="none"><use href="#brush" class="fill-blue"/></svg>
    <span class="label" style="padding-left:16px;">Interior - Exterior - Cabinet</span>
  </div>

  <div class="wordmark" style="left:276px; top:612px; font-size:80px;">Lark</div>

  <div class="band" style="left:320px; top:722px; width:216px; height:30px; font-size:11px;">
    <svg class="stroke" viewBox="0 0 100 20" preserveAspectRatio="none"><use href="#brush" class="fill-orange"/></svg>
    <span class="label" style="padding-left:26px; gap:6px;"><svg class="icon" width="13" height="13" viewBox="0 0 20 20"><use href="#phone-icon"/></svg>(927) 555-LARK</span>
  </div>

  <div class="band" style="left:256px; top:750px; width:284px; height:30px; font-size:11px;">
    <svg class="stroke" viewBox="0 0 100 20" preserveAspectRatio="none"><use href="#brush" class="fill-green"/></svg>
    <span class="label" style="padding-left:86px; gap:6px;"><svg class="icon" width="13" height="13" viewBox="0 0 20 20"><use href="#web-icon"/></svg>www.larkpainting.example</span>
  </div>
</section>

<!-- Hood layout -->
<section class="layout hood-layout" aria-label="Hood layout">
  <div class="zone hood-zone" aria-hidden="true"></div>
  <div class="wordmark" style="left:784px; top:634px; font-size:44px;">Lark</div>
</section>

</body>
</html>
```